Redesign our current website with a more professional feel

We currently have a running website that generates some traffic and looks ok but now we want to revamp it with professional eye catching design.
We are open to proposals and open to any new ideas or suggestions but we have to see your previous work.
our current site is www.kelbrin-works.com.au

Thank you for your time and we look forward to seeing your proposals

Target Market(s)

Business owners, managers

Industry/Entity Type

Security

Number of Pages Required

5+ page

```html
<!DOCTYPE html>
<html lang="en">
<head>
<meta charset="utf-8">
<title>Kelbrin Works – Security Services</title>
<link href="https://fonts.googleapis.com/css2?family=Raleway:wght@400;500;600;700&family=Open+Sans:wght@400;600&display=swap" rel="stylesheet">
<style>
:root{
  --blue:#5b86c9;
  --blue-dark:#1f4590;
  --navy:#1c3f8f;
  --orange:#f6ad3b;
  --red:#d8282c;
  --red-dark:#b91f24;
  --text:#333;
  --muted:#777;
  --light:#f4f4f4;
  --line:#e2e2e2;
  --footer:#3c3c3c;
  --footer-deep:#2d2d2d;
  --footer-text:#bdbdbd;
}
*{box-sizing:border-box;margin:0;padding:0}
html,body{width:1200px;height:2946px;overflow:hidden}
body{font-family:"Open Sans",Arial,sans-serif;color:var(--text);background:#fff;position:relative}
h1,h2,h3,h4,.raleway{font-family:"Raleway",Arial,sans-serif}
section,header,footer{position:relative;width:1200px}

/* header */
.site-header{height:128px}
.quote-call{position:absolute;left:160px;top:46px;text-align:right;width:200px;white-space:nowrap}
.quote-call small{display:block;font-size:13px;color:#999}
.quote-call strong{display:block;font-family:"Raleway",sans-serif;font-size:17px;color:var(--blue);font-weight:600;margin-top:4px}
.brand{position:absolute;left:512px;top:24px;width:180px;height:80px;display:flex;align-items:center;justify-content:center;gap:10px}
.brand-dot{width:20px;height:20px;border-radius:50%;background:var(--navy)}
.brand-name{font-family:"Raleway",sans-serif;font-weight:700;font-size:30px;color:var(--navy);letter-spacing:1px}
.social{position:absolute;left:840px;top:54px;display:flex;gap:6px}
.social span{width:20px;height:20px;border-radius:50%;background:#b5b5b5}

.main-nav{height:35px;background:var(--blue);display:flex;justify-content:center;padding-left:56px}
.main-nav a{font-family:"Raleway",sans-serif;font-size:11px;font-weight:600;color:#fff;text-decoration:none;text-transform:uppercase;line-height:35px;padding:0 17px}
.main-nav a.active{background:var(--orange)}

/* hero */
.hero{height:361px;background:linear-gradient(180deg,#4a4f57 0%,#2f3238 55%,#3b3e44 100%)}
.hero-photo{position:absolute;inset:0}
.hero-title{position:absolute;top:155px;width:100%;text-align:center;color:#fff;font-family:"Raleway",sans-serif}
.hero-title .l1{font-size:24px;font-weight:600}
.hero-title .l2{font-size:20px;font-weight:500;margin-top:2px}
.hero-arrow{position:absolute;top:170px}

/* tabs */
.tabs{height:95px;background:#fff;display:flex;border-bottom:1px solid var(--line)}
.tab{flex:1;text-align:center;padding-top:22px;font-family:"Raleway",sans-serif;font-size:13px;color:#a5a5a5;text-transform:uppercase;letter-spacing:.5px}
.tab.current{flex:0 0 402px;border-left:1px solid var(--line);border-right:1px solid var(--line);border-bottom:4px solid var(--orange);font-size:19px;color:#444;font-weight:500;position:relative}
.tab.current::before{content:"";position:absolute;top:-14px;left:50%;margin-left:-14px;border:14px solid transparent;border-top:0;border-bottom-color:#fff}
.tab svg{display:block;margin:0 auto 10px}

/* about */
.about{height:339px}
.about-photo{position:absolute;left:232px;top:57px;width:226px;height:227px;background:linear-gradient(135deg,#c9d4de 0%,#8e9aab 45%,#e9e3da 100%)}
.about-text{position:absolute;left:560px;top:56px;width:410px}
.about-text h2{font-size:23px;font-weight:500;color:#333;line-height:29px}
.about-text p{font-size:11px;color:#777;line-height:16px;margin-top:22px}
.btn{display:inline-block;background:var(--blue);color:#fff;font-family:"Raleway",sans-serif;font-weight:600;font-size:10px;text-transform:uppercase;padding:0 15px;line-height:26px;text-decoration:none}
.about-text .btn{margin-top:24px}

/* why us */
.why{height:270px;background:var(--light)}
.section-title{text-align:center;font-family:"Raleway",sans-serif;font-size:19px;font-weight:600;color:#333}
.why .section-title{padding-top:54px}
.features{display:flex;justify-content:space-between;width:900px;margin:34px auto 0}
.feature{width:280px;text-align:center}
.feature h4{font-size:12px;font-weight:700;color:#333;margin-top:12px}
.feature p{font-size:11px;color:#777;line-height:15px;margin-top:8px}

/* areas */
.areas{height:337px}
.areas .section-title{padding-top:55px}
.area-grid{position:absolute;top:104px;left:157px;display:flex;gap:25px}
.area{width:279px;height:176px;position:relative;display:flex;align-items:center;justify-content:center;color:#fff;font-family:"Raleway",sans-serif;font-weight:700;font-size:13px;text-transform:uppercase}
.area.sydney{background:linear-gradient(180deg,#b88ab7 0%,#7b5c8d 55%,#3d3552 100%)}
.area.melbourne{background:linear-gradient(180deg,#4f6c8a 0%,#2c3c52 60%,#4b4030 100%)}
.area.melbourne .frame{position:absolute;left:8px;top:8px;right:8px;bottom:8px;border:1px solid rgba(255,255,255,.85)}
.area.nation{background:linear-gradient(180deg,#cfe2f2 0%,#6b91b8 55%,#2a4e78 100%)}
.area .label{position:relative;text-align:center}
.area .go{display:block;margin:16px auto 0}

/* testimonial */
.testimonial{height:307px;background:var(--blue-dark);text-align:center;color:#fff}
.testimonial svg{margin-top:56px}
.testimonial blockquote{font-family:"Raleway",sans-serif;font-size:19px;line-height:25px;margin-top:28px}
.testimonial cite{display:block;font-style:normal;font-size:13px;margin-top:22px}
.testimonial cite small{display:block;font-size:9px;opacity:.8;margin-top:3px}

/* offers */
.offers{height:430px}
.offers .section-title{padding-top:54px}
.offer-grid{position:absolute;top:102px;left:157px;display:flex;gap:25px}
.offer{width:279px;height:271px;background:#fff;border:1px solid #e6e6e6;box-shadow:0 1px 4px rgba(0,0,0,.08);text-align:center;position:relative}
.offer-head{height:104px;position:relative;color:#fff;font-family:"Raleway",sans-serif}
.offer-head svg{position:absolute;left:-1px;top:-1px}
.offer-head .price{position:relative;font-size:23px;font-weight:700;padding-top:18px}
.offer-head .note{position:relative;font-size:18px;line-height:22px}
.offer h4{font-size:14px;font-weight:700;margin-top:16px;color:#333}
.offer p{font-size:11px;color:#666;line-height:14px;margin-top:2px;padding:0 24px}
.offer .btn{margin-top:14px;font-size:9px;line-height:24px;padding:0 18px}
.offer .btn.hot{background:var(--orange)}
.offer .cond{position:absolute;bottom:22px;left:0;right:0;font-size:8px;color:var(--red);text-transform:uppercase}
.offer .cond::before,.offer .cond::after{content:"";display:inline-block;width:36px;height:1px;background:#ddd;vertical-align:middle;margin:0 6px}

/* cta */
.cta{height:192px;background:var(--light);text-align:center}
.cta h3{font-size:19px;font-weight:600;color:#333;padding-top:40px;text-transform:uppercase}
.cta p{font-size:14px;color:#555;margin-top:4px}
.cta .actions{margin-top:24px;display:flex;justify-content:center;gap:10px}
.cta .btn{font-size:11px;line-height:32px;padding:0 18px;box-shadow:0 2px 0 #4a71ad}

/* footer */
.site-footer{height:373px;background:var(--footer);color:var(--footer-text)}
.foot-col{position:absolute;top:52px}
.foot-col h5{font-family:"Raleway",sans-serif;font-size:13px;font-weight:600;color:#fff;text-transform:uppercase;padding-bottom:10px;border-bottom:1px solid #5a5a5a;width:279px}
.news-item{display:flex;gap:14px;margin-top:22px}
.news-thumb{width:52px;height:52px;border-radius:50%;background:linear-gradient(135deg,#8a7a6a,#2e2a26)}
.news-item p{font-size:11px;line-height:14px;color:#ddd}
.news-item p.hl{color:var(--orange)}
.news-item time{display:block;font-size:10px;color:#999;margin-top:6px}
.view-more{display:block;font-size:9px;font-weight:600;color:var(--blue);margin-top:18px;text-transform:uppercase}
.newsletter p{font-size:11px;color:#ccc;line-height:15px;margin-top:26px}
.newsletter .field{width:204px;height:24px;border:1px solid #6a6a6a;background:#444;font-size:10px;color:#999;padding-left:8px;line-height:22px;margin-top:12px}
.newsletter .btn{margin-top:22px;font-size:9px;line-height:22px;padding:0 20px}
.contact p{font-size:11px;color:#ccc;line-height:14px;margin-top:16px}
.contact p:first-of-type{margin-top:26px}
.contact .social{position:static;margin-top:18px}
.contact .social span{background:#d5d5d5;width:22px;height:22px}
.to-top{position:absolute;left:1082px;top:68px}

.bottom-bar{height:79px;background:var(--footer-deep);font-size:11px;color:#aaa}
.bottom-bar .copy{position:absolute;left:157px;top:32px}
.bottom-bar nav{position:absolute;left:471px;top:32px}
.bottom-bar nav span{color:#777;margin:0 6px}
.bottom-bar nav a{color:#aaa;text-decoration:none}
.bottom-bar nav a.hl{color:var(--orange)}
</style>
</head>
<body>

<header class="site-header">
  <div class="quote-call"><small>Call Now for a Free Quote</small><strong>1300 44 2190</strong></div>
  <div class="brand"><span class="brand-dot"></span><span class="brand-name">KELBRIN</span></div>
  <div class="social"><span></span><span></span><span></span><span></span></div>
</header>
<nav class="main-nav">
  <a class="active" href="#">Home</a><a href="#">About</a><a href="#">Services</a><a href="#">Special Offers</a><a href="#">News</a><a href="#">Employment</a><a href="#">Contact Us</a>
</nav>

<section class="hero">
  <div class="hero-photo" role="img" aria-label="Two uniformed security guards standing in front of branded mobile patrol cars"></div>
  <div class="hero-title"><div class="l1">Mobile Patrol Vehicles to Help</div><div class="l2">Minimise the Threat to Your Business and Property</div></div>
  <svg class="hero-arrow" style="left:92px" width="26" height="22" viewBox="0 0 26 22"><path d="M12 2 3 11l9 9M3 11h21" fill="none" stroke="#fff" stroke-width="2.5"/></svg>
  <svg class="hero-arrow" style="left:1082px" width="26" height="22" viewBox="0 0 26 22"><path d="m14 2 9 9-9 9M23 11H2" fill="none" stroke="#fff" stroke-width="2.5"/></svg>
</section>

<div class="tabs">
  <div class="tab"><svg width="24" height="22" viewBox="0 0 24 22"><rect x="2" y="2" width="20" height="13" fill="#bbb"/><rect x="8" y="16" width="8" height="4" fill="#bbb"/></svg>Control Room</div>
  <div class="tab current"><svg width="34" height="30" viewBox="0 0 34 30"><circle cx="17" cy="8" r="6" fill="var(--orange)"/><rect x="4" y="16" width="26" height="12" rx="2" fill="var(--orange)"/></svg>Mobile Patrols</div>
  <div class="tab"><svg width="22" height="24" viewBox="0 0 22 24"><circle cx="11" cy="6" r="5" fill="#bbb"/><rect x="3" y="13" width="16" height="10" rx="2" fill="#bbb"/></svg>Static Guarding</div>
</div>

<section class="about">
  <div class="about-photo" role="img" aria-label="Business people shaking hands across a meeting table"></div>
  <div class="about-text">
    <h2>At Kelbrin Works<br>Our Focus in on Services Delivery<br>and Client Satisfaction.</h2>
    <p>We approach business with a sense of partnership and seek to understand each individual customer's requirements We achieve this goal by teamwork, accountability and integrity.</p>
    <a class="btn" href="#">About Us</a>
  </div>
</section>

<section class="why">
  <h2 class="section-title">Why People Choose Us?</h2>
  <div class="features">
    <div class="feature">
      <svg width="42" height="42" viewBox="0 0 42 42"><circle cx="21" cy="21" r="19" fill="none" stroke="var(--blue)" stroke-width="2"/><text x="21" y="29" text-anchor="middle" font-family="Raleway,sans-serif" font-size="22" fill="var(--blue)">$</text></svg>
      <h4>Affordable Peace of Mind</h4>
      <p>Lorem Ipsum is simply dummy text of the<br>printing and typesetting industry.</p>
    </div>
    <div class="feature">
      <svg width="42" height="42" viewBox="0 0 42 42"><circle cx="21" cy="21" r="19" fill="none" stroke="var(--orange)" stroke-width="2"/><path d="m12 21 6 6 12-12" fill="none" stroke="var(--orange)" stroke-width="2"/></svg>
      <h4>Dependable Security</h4>
      <p>Lorem Ipsum is simply dummy text of the<br>printing and typesetting industry.</p>
    </div>
    <div class="feature">
      <svg width="44" height="42" viewBox="0 0 44 42"><path d="M22 38 5 20C-1 12 5 3 13 4c4 0 7 3 9 6 2-3 5-6 9-6 8-1 14 8 8 16Z" fill="none" stroke="var(--blue)" stroke-width="2"/></svg>
      <h4>Custom Care</h4>
      <p>Lorem Ipsum is simply dummy text of the<br>printing and typesetting industry.</p>
    </div>
  </div>
</section>

<section class="areas">
  <h2 class="section-title">Areas We Protect</h2>
  <div class="area-grid">
    <div class="area sydney" role="img" aria-label="Harbour city skyline at dusk"><span class="label">Sydney</span></div>
    <div class="area melbourne" role="img" aria-label="City skyline over the river at night"><span class="frame"></span><span class="label">Melbourne<svg class="go" width="22" height="22" viewBox="0 0 22 22"><circle cx="11" cy="11" r="11" fill="var(--orange)"/><path d="M6 11h9m-4-4 4 4-4 4" fill="none" stroke="#fff" stroke-width="2"/></svg></span></div>
    <div class="area nation" role="img" aria-label="Glass office towers seen from below"><span class="label">Nationwide for Business</span></div>
  </div>
</section>

<section class="testimonial">
  <svg width="100" height="72" viewBox="0 0 100 72"><path d="M4 36C4 16 14 4 34 2v12c-8 2-12 8-12 16h12v40H4Z M56 36C56 16 66 4 86 2v12c-8 2-12 8-12 16h12v40H56Z" fill="#3d5fa3"/></svg>
  <blockquote>Kelbrin Works have a very capable and hard working team<br>who always meet or exceed client expectations.</blockquote>
  <cite>- Daniel Reyes<small>(Sr. Environmental Engineer)</small></cite>
</section>

<section class="offers">
  <h2 class="section-title">Get Special offer</h2>
  <div class="offer-grid">
    <div class="offer">
      <div class="offer-head"><svg width="279" height="104" viewBox="0 0 279 104"><polygon points="0,0 279,0 279,84 139.5,104 0,84" fill="var(--red)"/><polygon points="0,0 120,0 0,60" fill="var(--red-dark)"/></svg><div class="price">$40 Per Month</div><div class="note">Installed*</div></div>
      <h4>Business Intruder Alarm</h4>
      <p>Professional &amp; Zone Alarm Panel for Your Safety &amp; Security</p>
      <a class="btn" href="#">Learn More</a>
      <div class="cond">*Condition Apply</div>
    </div>
    <div class="offer">
      <div class="offer-head"><svg width="279" height="104" viewBox="0 0 279 104"><polygon points="0,0 279,0 279,84 139.5,104 0,84" fill="var(--red)"/><polygon points="0,0 120,0 0,60" fill="var(--red-dark)"/></svg><div class="price" style="padding-top:30px;font-size:22px">3 Months Free</div></div>
      <h4>Back to Base Alrm Monitoring</h4>
      <p>with All New Installations</p>
      <a class="btn hot" href="#" style="margin-top:28px">Learn More</a>
      <div class="cond">*Condition Apply</div>
    </div>
    <div class="offer">
      <div class="offer-head"><svg width="279" height="104" viewBox="0 0 279 104"><polygon points="0,0 279,0 279,84 139.5,104 0,84" fill="var(--red)"/><polygon points="0,0 120,0 0,60" fill="var(--red-dark)"/></svg><div class="price">$80 Per Month</div><div class="note">Installed*</div></div>
      <h4>CCTV Package</h4>
      <p>CCTV that can be Viewed from Home and Office on Your smartphone</p>
      <a class="btn" href="#">Learn More</a>
      <div class="cond">*Condition Apply</div>
    </div>
  </div>
</section>

<section class="cta">
  <h3>Have a Question or Need a Free Quote?</h3>
  <p>Contact us and we will get to you as soon as possible. / or just give us a call.</p>
  <div class="actions">
    <a class="btn" href="#">Get a Free Quote &nbsp;&#9656;</a>
    <a class="btn" href="#"><svg width="11" height="11" viewBox="0 0 11 11" style="vertical-align:-1px"><path d="M2 0 4 3 3 4.5c.8 1.6 2 2.8 3.5 3.5L8 7l3 2-1.2 2C5 11 0 6 0 1.2Z" fill="#fff"/></svg>&nbsp; Call: 1300 44 2190</a>
  </div>
</section>

<footer class="site-footer">
  <div class="foot-col" style="left:157px">
    <h5>Latest News</h5>
    <div class="news-item"><div class="news-thumb" role="img" aria-label="News thumbnail photo"></div><div><p>Phasellus Luctus Ante Ante,<br>At Vehicula Quam ...</p><time>20 Apr'15</time></div></div>
    <div class="news-item"><div class="news-thumb" role="img" aria-label="News thumbnail photo"></div><div><p class="hl">Phasellus Luctus Ante Ante,<br>At Vehicula Quam ...</p><time>18 April '15</time></div></div>
    <div class="news-item"><div class="news-thumb" role="img" aria-label="News thumbnail photo"></div><div><p>Phasellus Luctus Ante Ante,<br>At Vehicula Quam ...</p><time>06 April '15</time></div></div>
    <a class="view-more">View More &nbsp;&#10148;</a>
  </div>
  <div class="foot-col newsletter" style="left:461px">
    <h5>Newsletter</h5>
    <p>Join the Community to be<br>updated firstly?</p>
    <div class="field">Name</div>
    <div class="field">Email</div>
    <a class="btn" href="#">Subscribe</a>
  </div>
  <div class="foot-col contact" style="left:764px">
    <h5>Contact Info</h5>
    <p>Kelbrin Works<br>Suite 5/ 12 Harlow Street<br>Carrowvale, 2163</p>
    <p>Phone:<br>1300 44 2190</p>
    <p>Email:<br>info@kelbrin-works.com.au</p>
    <div class="social"><span></span><span></span><span></span><span></span></div>
  </div>
  <svg class="to-top" width="24" height="24" viewBox="0 0 24 24"><circle cx="12" cy="12" r="10" fill="none" stroke="#999" stroke-width="2"/><path d="M12 17V7m-4 4 4-4 4 4" fill="none" stroke="#999" stroke-width="2"/></svg>
</footer>
<div class="bottom-bar" style="position:relative">
  <div class="copy">© Kelbrin Works 2016. All right reserved.</div>
  <nav><a href="#">Home</a><span>/</span><a class="hl" href="#">Alarm &amp; CCTV Systems</a><span>/</span><a href="#">Home &amp; Corporate Security</a><span>/</span><a href="#">Policy</a><span>/</span><a href="#">T&amp;C's</a><span>/</span><a href="#">Sitemap</a></nav>
</div>

</body>
</html>
```